Flyer Design Project for lawn care business

I need a flyer designed for my lawn care business, "Hadley's Groundskeeping Services".  It is a family owned small landscaping company. I was thinking something that I can print  2- 3 per page.
I have  2 different logos I can upload to give an idea.  I have seen some I like that are colorfull with neat graphics but I also like some that are simple and elegant.  I would like something that catches your eye and looks professionaly done.

Target Market(s)
Homeowners in Durham, North Carolina with homes usually valued $200,000 or more.
Industry/Entity Type
Landscaping
Requirements
Must have
- I would like the address of my website listed on it, www.hadleygroundskeepingservices.example
I would like for it to say somewhere, 50% off first service with seasonal service.
Not sure if I want to list some of the services that I offer or just say full service lawn care.
Nice to have
- I have a logo with a bull pushing a lawn mower.  I live in Durham, NC also known as the Bull City.  I am not in love with the logo so feel free to change it or not use it at all.

```html
<!DOCTYPE html>
<html lang="en">
<head>
<meta charset="utf-8">
<title>Hadley's Groundskeeping Services – Flyer Sheet</title>
<link href="https://fonts.googleapis.com/css2?family=Oswald:wght@500&family=Roboto:ital,wght@0,700;0,900;1,900&display=swap" rel="stylesheet">
<style>
  :root{
    --sheet:#ffffff;
    --edge:#c9c9c9;
    --offer-red:#e5252a;
    --leaf-green:#6fb43f;
    --deep-green:#2f6b1e;
    --sun-yellow:#f4e21a;
    --ink:#1d1d1d;
    --white:#ffffff;
    --photo-top:#5f9636;
    --photo-mid:#6fa645;
    --photo-low:#9cc478;
  }
  *{margin:0;padding:0;box-sizing:border-box}
  html,body{width:848px;height:1200px;overflow:hidden;background:var(--sheet)}
  .sheet{position:relative;width:848px;height:1200px;background:var(--sheet)}

  .flyer{
    position:absolute;
    container-type:size;
    background:var(--white);
    border:1px solid var(--edge);
    overflow:hidden;
    font-family:"Roboto",Arial,sans-serif;
  }
  .flyer--left{left:34px;top:30px;width:316px;height:726px}
  .flyer--right{left:434px;top:30px;width:316px;height:726px}
  .flyer-slot{position:absolute;left:64px;top:784px;width:716px;height:380px}
  .flyer--turned{left:168px;top:-168px;width:380px;height:716px;transform:rotate(90deg)}

  .garden-photo{
    position:absolute;left:0;top:0;width:100%;height:80%;
    background:linear-gradient(to bottom,var(--photo-top) 0%,var(--photo-mid) 55%,var(--photo-low) 82%,var(--white) 100%);
  }

  .offer{position:absolute;left:0;width:100%;text-align:center;line-height:1;white-space:nowrap}
  .offer-deal{
    top:30.5%;font-size:14cqw;font-weight:900;font-style:italic;color:var(--offer-red);
    -webkit-text-stroke:0.5cqw var(--white);paint-order:stroke fill;
  }
  .offer-first{top:37.4%;font-size:8cqw;font-weight:900;color:var(--white);text-shadow:0 0 1cqw rgba(0,0,0,.6)}
  .offer-with{top:41.6%;font-size:4cqw;font-weight:700;color:var(--white);text-shadow:0 0 1cqw rgba(0,0,0,.6)}
  .offer-seasonal{
    top:44%;font-size:7cqw;font-weight:700;color:var(--leaf-green);
    -webkit-text-stroke:0.35cqw var(--ink);paint-order:stroke fill;
  }

  .headline{position:absolute;left:0;width:100%;text-align:center;line-height:1;white-space:nowrap}
  .headline-full{
    top:57.8%;font-size:9cqw;font-weight:900;color:var(--sun-yellow);
    -webkit-text-stroke:0.6cqw var(--ink);paint-order:stroke fill;
  }
  .headline-lawn{
    top:62.6%;font-family:"Oswald","Arial Narrow",sans-serif;font-weight:500;font-size:14cqw;color:var(--white);
    -webkit-text-stroke:0.6cqw var(--deep-green);paint-order:stroke fill;
  }

  .brand{position:absolute;left:7%;top:81.5%;width:88%;display:flex;align-items:center;gap:3cqw}
  .brand-mark{flex:0 0 auto;width:13cqw;height:13cqw;background:var(--leaf-green)}
  .brand-body{flex:1}
  .brand-name{font-size:5.8cqw;font-weight:900;color:var(--leaf-green);line-height:1.05}
  .brand-phone{font-size:3.6cqw;font-weight:700;color:var(--deep-green);text-align:right;margin-top:1cqw}
  .brand-services{position:absolute;left:7%;top:92%;font-size:3cqw;font-weight:700;color:var(--offer-red);white-space:nowrap}
  .website{position:absolute;left:0;bottom:2.4%;width:100%;text-align:center;font-size:3.9cqw;font-weight:700;color:var(--deep-green);white-space:nowrap}
</style>
</head>
<body>
<main class="sheet">

  <article class="flyer flyer--left">
    <div class="garden-photo" role="img" aria-label="Photo placeholder: garden path between lawns and trimmed hedges"></div>
    <p class="offer offer-deal">50% off</p>
    <p class="offer offer-first">first service</p>
    <p class="offer offer-with">with</p>
    <p class="offer offer-seasonal">seasonal service</p>
    <p class="headline headline-full">FULL SERVICE</p>
    <p class="headline headline-lawn">Lawn Care</p>
    <div class="brand">
      <span class="brand-mark"></span>
      <div class="brand-body">
        <p class="brand-name">Hadley's Groundskeeping Services</p>
        <p class="brand-phone">(919) 555-0147</p>
      </div>
    </div>
    <p class="brand-services">Carpentry • Plumbing • HVAC • Lawn Care</p>
    <p class="website">www.hadleygroundskeepingservices.example</p>
  </article>

  <article class="flyer flyer--right">
    <div class="garden-photo" role="img" aria-label="Photo placeholder: garden path between lawns and trimmed hedges"></div>
    <p class="offer offer-deal">50% off</p>
    <p class="offer offer-first">first service</p>
    <p class="offer offer-with">with</p>
    <p class="offer offer-seasonal">seasonal service</p>
    <p class="headline headline-full">FULL SERVICE</p>
    <p class="headline headline-lawn">Lawn Care</p>
    <div class="brand">
      <span class="brand-mark"></span>
      <div class="brand-body">
        <p class="brand-name">Hadley's Groundskeeping Services</p>
        <p class="brand-phone">(919) 555-0147</p>
      </div>
    </div>
    <p class="brand-services">Carpentry • Plumbing • HVAC • Lawn Care</p>
    <p class="website">www.hadleygroundskeepingservices.example</p>
  </article>

  <div class="flyer-slot">
    <article class="flyer flyer--turned">
      <div class="garden-photo" role="img" aria-label="Photo placeholder: garden path between lawns and trimmed hedges"></div>
      <p class="offer offer-deal">50% off</p>
      <p class="offer offer-first">first service</p>
      <p class="offer offer-with">with</p>
      <p class="offer offer-seasonal">seasonal service</p>
      <p class="headline headline-full">FULL SERVICE</p>
      <p class="headline headline-lawn">Lawn Care</p>
      <div class="brand">
        <span class="brand-mark"></span>
        <div class="brand-body">
          <p class="brand-name">Hadley's Groundskeeping Services</p>
          <p class="brand-phone">(919) 555-0147</p>
        </div>
      </div>
      <p class="brand-services">Carpentry • Plumbing • HVAC • Lawn Care</p>
      <p class="website">www.hadleygroundskeepingservices.example</p>
    </article>
  </div>

</main>
</body>
</html>
```